Healthcare food company need product packaging design

We need a food supplements product packaging design for an all natural wholesome food.
For natural wholesome design, we need a fresh and clean looking label as the products contain soybean, kale and broccoli as an alternative protein food powder. To appeal to the health conscious consumer .

Target Market(s)

For natural wholesome food, all age group

Industry/Entity Type

Health And Wellness

Font styles to use
Serif
Sans Serif

Requirements
Must have
• Strong colours and bigger font size to attract consumer when product is placed on shelf
Nice to have
• Fresh vegetable colours with elements of green or mutiple colours
Should not have
• No restriction

```html
<!DOCTYPE html>
<html lang="en">
<head>
<meta charset="utf-8">
<title>All Plant Source Protein Powder – Label Options</title>
<link href="https://fonts.googleapis.com/css2?family=Open+Sans:wght@400;600;700&family=Arimo:wght@400;700&family=Tinos:wght@400;700&display=swap" rel="stylesheet">
<style>
  :root{
    --page:#ffffff;
    --leaf-dark:#1f5a12;
    --leaf:#2f7d18;
    --leaf-light:#8fd13a;
    --ink-dark:#1d2a1a;
    --red:#ec1c24;
    --magenta:#e8138f;
    --navy:#1d1f8a;
    --cyan:#5fd7ea;
    --orange:#f68b1f;
    --yellow:#f4f03a;
    --gold:#c9a43c;
    --dot-pink:#ec2a8e;
    --dot-orange:#f0552a;
    --dot-green:#5fe07a;
    --dot-cyan:#3fdcf0;
  }
  *{box-sizing:border-box;margin:0;padding:0}
  html,body{width:1200px;height:1124px;overflow:hidden;background:var(--page)}
  body{position:relative;font-family:"Arimo",Arial,sans-serif}

  .option-number{position:absolute;left:12px;font:400 13px "Arimo",Arial,sans-serif;color:var(--ink-dark)}

  .label{position:absolute;left:43px;width:1138px;height:350px;background:var(--page);overflow:hidden}
  .label--one{top:6px;--about-ink:var(--red);--contact-ink:var(--magenta);--tag:var(--cyan);--tag-arrow:#2f55e0;--swoosh:var(--leaf-light);--swoosh-soft:#c6ec86}
  .label--two{top:370px;--about-ink:var(--magenta);--contact-ink:var(--cyan);--tag:var(--red);--tag-arrow:var(--orange);--swoosh:var(--magenta);--swoosh-soft:#f7a8d6}
  .label--three{top:756px;--about-ink:var(--navy);--contact-ink:var(--navy);--tag:var(--red);--tag-arrow:var(--orange);--swoosh:var(--magenta);--swoosh-soft:#f7a8d6}

  .label__top-rule{position:absolute;left:0;top:0;width:100%;height:10px;background:var(--leaf)}
  .label__base-band{position:absolute;left:0;bottom:0;width:100%;height:12px;background:linear-gradient(90deg,var(--leaf-light),var(--leaf) 50%,var(--leaf-light))}

  .about{position:absolute;left:55px;top:44px;width:258px}
  .about__title{font:700 15px "Arimo",Arial,sans-serif;color:var(--ink-dark);margin-bottom:6px}
  .label--two .about__title{color:var(--magenta)}
  .label--three .about__title{color:var(--navy);border-bottom:1px solid #9aa0d8;padding-bottom:3px;width:140px}
  .about__text{font:700 10.6px/14.6px "Arimo",Arial,sans-serif;letter-spacing:-0.25px;color:var(--about-ink);text-align:justify}

  .company{position:absolute;left:72px;top:218px;font-family:"Tinos","Times New Roman",serif;color:var(--contact-ink)}
  .company__name{font-size:13px;font-weight:700}
  .company__line{font-size:9px;font-weight:700;line-height:12px}

  .front-panel{position:absolute;left:438px;top:0;width:256px;height:262px}
  .front-panel svg{position:absolute;left:0;top:0}
  .front-panel__title{position:absolute;left:0;top:14px;width:256px;text-align:center;color:#fff;font-family:"Open Sans",Arial,sans-serif;font-weight:600;line-height:1}
  .front-panel__title span{display:block}
  .front-panel__title .t-all{font-size:42px;letter-spacing:-0.5px}
  .front-panel__title .t-source{font-size:26.5px;margin-top:4px}
  .front-panel__title .t-powder{font-size:56px;margin-top:2px}
  .front-panel__weight{position:absolute;right:22px;top:148px;z-index:2;color:#fff;font:400 20px "Tinos",serif;line-height:1}
  .front-panel__brand{position:absolute;left:97px;top:172px;width:62px;height:62px;z-index:2;display:flex;align-items:center;justify-content:center;color:#fff;font:700 12px "Open Sans",Arial,sans-serif;letter-spacing:1px}

  .produce{position:absolute;left:280px;top:222px;width:590px;height:116px;border-radius:60px 60px 0 0;background:radial-gradient(ellipse at 50% 60%,#d6b37a 0 22%,#7cbf3a 40%,#3f8f22 70%,rgba(63,143,34,0) 100%)}
  .produce--corner-left{position:absolute;left:0;top:250px;width:120px;height:88px;border-radius:60px 60px 0 0;background:radial-gradient(ellipse at 50% 70%,#4f9a2a,rgba(79,154,42,0) 75%)}
  .produce--corner-right{position:absolute;right:0;top:250px;width:120px;height:88px;border-radius:60px 60px 0 0;background:radial-gradient(ellipse at 50% 70%,#4f9a2a,rgba(79,154,42,0) 75%)}

  .ribbon-stripes{position:absolute;top:10px}
  .wave-art{position:absolute;left:0;top:70px;width:470px;height:240px;background:radial-gradient(ellipse at 40% 70%,rgba(236,120,170,.35),rgba(246,210,120,.15) 50%,rgba(255,255,255,0) 75%)}

  .ingredients{position:absolute;left:859px;top:12px;width:194px;height:44px}
  .ingredients__tag{position:absolute;left:0;top:0;width:142px;height:44px;background:var(--tag);padding:3px 4px}
  .ingredients__arrows{position:absolute;left:140px;top:0}
  .ingredients__title{font:400 13px "Arimo",Arial,sans-serif;color:var(--ink-dark)}
  .label--two .ingredients__title,.label--three .ingredients__title,
  .label--two .ingredients__list,.label--three .ingredients__list{color:#fff}
  .ingredients__list{font:700 8.6px/10px "Arimo",Arial,sans-serif;color:var(--ink-dark)}

  .nutrition{position:absolute;left:859px;top:68px;width:160px;height:146px;background:var(--yellow);padding:4px 5px;font:700 7.2px/9px "Arimo",Arial,sans-serif;color:var(--ink-dark)}
  .nutrition__rule{border-top:1px solid #86b53a;margin:2px 0}

  .batch-frame{position:absolute;left:1027px;top:72px;width:56px;height:160px}
  .batch-frame__text{position:absolute;left:8px;top:150px;transform:rotate(-90deg);transform-origin:0 0;font:700 6px/11px "Arimo",Arial,sans-serif;color:var(--ink-dark);white-space:nowrap}

  .badges{position:absolute;left:859px;top:264px;display:flex;gap:6px}
  .badges span{width:22px;height:22px;border-radius:50%}
  .badges .b1{background:var(--dot-pink)}
  .badges .b2{background:var(--dot-orange)}
  .badges .b3{background:var(--dot-green)}
  .badges .b4{background:var(--dot-cyan)}
</style>
</head>
<body>

<div class="option-number" style="top:200px">01</div>
<div class="option-number" style="top:566px">02</div>
<div class="option-number" style="top:922px">03</div>

<!-- Option 01 -->
<section class="label label--one">
  <div class="label__top-rule"></div>
  <div class="about">
    <h2 class="about__title">About Product</h2>
    <p class="about__text">All plants source protein powderAll plants source protein powderAll plants source protein powderAll plants source protein powderAll plants source protein powderAll plants source protein powderAll plants source protein powderAll plants source protein powderAll plants source protein powderAll plants source protein powderAll plants source protein powderAll plants source protein powder</p>
  </div>
  <div class="company">
    <div class="company__name">Company name</div>
    <div class="company__line">Address</div>
    <div class="company__line">00000000</div>
    <div class="company__line">Tel : 00000000000</div>
    <div class="company__line">E-mail : hello@verde.lk</div>
    <div class="company__line">Web : 000000000000</div>
  </div>

  <div class="front-panel">
    <svg width="256" height="262" viewBox="0 0 256 262">
      <defs><linearGradient id="g1" x1="0" y1="0" x2="0" y2="1"><stop offset="0" stop-color="#2b6b14"/><stop offset="1" stop-color="#1d5210"/></linearGradient></defs>
      <path d="M0 0H256V212Q128 250 0 212Z" fill="url(#g1)"/>
      <path d="M0 184Q130 160 256 182V192Q130 172 0 198Z" fill="#fff"/>
      <path d="M0 196Q130 172 256 192V200Q130 182 0 208Z" fill="var(--swoosh)"/>
      <path d="M0 208Q130 186 256 204V210Q130 194 0 216Z" fill="var(--swoosh-soft)"/>
      <circle cx="128" cy="203" r="31" fill="#2b6b14" stroke="#fff" stroke-width="2"/>
    </svg>
    <h1 class="front-panel__title"><span class="t-all">ALL PLANT</span><span class="t-source">SOURCE PROTEIN</span><span class="t-powder">POWDER</span></h1>
    <div class="front-panel__weight">300g</div>
    <div class="front-panel__brand">VERDE</div>
  </div>

  <div class="produce" role="img" aria-label="Photo of soybeans, edamame pods, kale and broccoli"></div>
  <div class="produce--corner-left" role="img" aria-label="Photo of kale leaves"></div>
  <div class="produce--corner-right" role="img" aria-label="Photo of kale leaves"></div>

  <div class="ingredients">
    <div class="ingredients__tag">
      <div class="ingredients__title">Ingredients</div>
      <div class="ingredients__list">soybean, kale and broccoli<br>No Additives or Preservatives</div>
    </div>
    <svg class="ingredients__arrows" width="52" height="44" viewBox="0 0 52 44">
      <path d="M0 0H22L34 22L22 44H0Z" fill="var(--tag)"/>
      <path d="M24 0H34L46 22L34 44H24L36 22Z" fill="var(--tag-arrow)"/>
    </svg>
  </div>

  <div class="nutrition">
    Serving Size of 1 Tablespoon<br>Serving Per Container
    <div class="nutrition__rule"></div>
    Amount Per Serving<br>Calaries 125 Calaries from Fat 125
    <div class="nutrition__rule"></div>
    Total Fat 00<br>Saturated Fat 00<br>Polyunsturated Fat 00<br>Monounsaturated Fat 00<br>Cholostrerol 00 mg<br>Dodelum 00mg<br>Total Carbohydrates 00g<br>Protein 00 mg
  </div>

  <div class="batch-frame">
    <svg width="56" height="160" viewBox="0 0 56 160"><rect x="2" y="2" width="52" height="156" rx="8" fill="none" stroke="var(--gold)" stroke-width="2"/></svg>
    <div class="batch-frame__text">Best before :<br>Date of manufactured :<br>Batch No :<br>Maximum Price :</div>
  </div>

  <div class="badges"><span class="b1"></span><span class="b2"></span><span class="b3"></span><span class="b4"></span></div>
  <div class="label__base-band"></div>
</section>

<!-- Option 02 -->
<section class="label label--two">
  <div class="label__top-rule"></div>
  <svg class="ribbon-stripes" style="left:325px" width="110" height="130" viewBox="0 0 110 130">
    <path d="M0 0H14V60L0 80Z" fill="#f4b07a" opacity=".8"/>
    <path d="M18 0H32V90L18 110Z" fill="#f6a5c8" opacity=".8"/>
    <path d="M36 0H50V100L36 120Z" fill="#9de3f0" opacity=".8"/>
    <path d="M54 0H68V110L54 130Z" fill="#f7d27a" opacity=".8"/>
    <path d="M72 0H86V95L72 115Z" fill="#b8e38a" opacity=".8"/>
    <path d="M90 0H104V80L90 100Z" fill="#f49a8a" opacity=".8"/>
  </svg>
  <svg class="ribbon-stripes" style="left:700px" width="110" height="130" viewBox="0 0 110 130">
    <path d="M0 0H14V80L0 100Z" fill="#f49a8a" opacity=".8"/>
    <path d="M18 0H32V95L18 115Z" fill="#b8e38a" opacity=".8"/>
    <path d="M36 0H50V110L36 130Z" fill="#f7d27a" opacity=".8"/>
    <path d="M54 0H68V100L54 120Z" fill="#9de3f0" opacity=".8"/>
    <path d="M72 0H86V90L72 110Z" fill="#f6a5c8" opacity=".8"/>
    <path d="M90 0H104V60L90 80Z" fill="#f49a8a" opacity=".8"/>
  </svg>
  <div class="about">
    <h2 class="about__title">About Product</h2>
    <p class="about__text">All plants source protein powderAll plants source protein powderAll plants source protein powderAll plants source protein powderAll plants source protein powderAll plants source protein powderAll plants source protein powderAll plants source protein powderAll plants source protein powderAll plants source protein powderAll plants source protein powderAll plants source protein powder</p>
  </div>
  <div class="company">
    <div class="company__name">Company name</div>
    <div class="company__line">Address</div>
    <div class="company__line">00000000</div>
    <div class="company__line">Tel : 00000000000</div>
    <div class="company__line">E-mail : hello@verde.lk</div>
    <div class="company__line">Web : 000000000000</div>
  </div>

  <div class="front-panel">
    <svg width="256" height="262" viewBox="0 0 256 262">
      <defs><linearGradient id="g2" x1="0" y1="0" x2="0" y2="1"><stop offset="0" stop-color="#2b6b14"/><stop offset="1" stop-color="#1d5210"/></linearGradient></defs>
      <path d="M0 0H256V212Q128 250 0 212Z" fill="url(#g2)"/>
      <path d="M0 184Q130 160 256 182V192Q130 172 0 198Z" fill="#fff"/>
      <path d="M0 196Q130 172 256 192V200Q130 182 0 208Z" fill="var(--swoosh)"/>
      <path d="M0 208Q130 186 256 204V210Q130 194 0 216Z" fill="var(--swoosh-soft)"/>
      <circle cx="128" cy="203" r="31" fill="#2b6b14" stroke="#fff" stroke-width="2"/>
    </svg>
    <h1 class="front-panel__title"><span class="t-all">ALL PLANT</span><span class="t-source">SOURCE PROTEIN</span><span class="t-powder">POWDER</span></h1>
    <div class="front-panel__weight">300g</div>
    <div class="front-panel__brand">VERDE</div>
  </div>

  <div class="produce" role="img" aria-label="Photo of soybeans, edamame pods, kale and broccoli"></div>
  <div class="produce--corner-left" role="img" aria-label="Photo of kale leaves"></div>
  <div class="produce--corner-right" role="img" aria-label="Photo of kale leaves"></div>

  <div class="ingredients">
    <div class="ingredients__tag">
      <div class="ingredients__title">Ingredients</div>
      <div class="ingredients__list">soybean, kale and broccoli<br>No Additives or Preservatives</div>
    </div>
    <svg class="ingredients__arrows" width="52" height="44" viewBox="0 0 52 44">
      <path d="M0 0H22L34 22L22 44H0Z" fill="var(--tag)"/>
      <path d="M24 0H34L46 22L34 44H24L36 22Z" fill="var(--tag-arrow)"/>
    </svg>
  </div>

  <div class="nutrition">
    Serving Size of 1 Tablespoon<br>Serving Per Container
    <div class="nutrition__rule"></div>
    Amount Per Serving<br>Calaries 125 Calaries from Fat 125
    <div class="nutrition__rule"></div>
    Total Fat 00<br>Saturated Fat 00<br>Polyunsturated Fat 00<br>Monounsaturated Fat 00<br>Cholostrerol 00 mg<br>Dodelum 00mg<br>Total Carbohydrates 00g<br>Protein 00 mg
  </div>

  <div class="batch-frame">
    <svg width="56" height="160" viewBox="0 0 56 160"><rect x="2" y="2" width="52" height="156" rx="8" fill="none" stroke="var(--gold)" stroke-width="2"/></svg>
    <div class="batch-frame__text">Best before :<br>Date of manufactured :<br>Batch No :<br>Maximum Price :</div>
  </div>

  <div class="badges"><span class="b1"></span><span class="b2"></span><span class="b3"></span><span class="b4"></span></div>
  <div class="label__base-band"></div>
</section>

<!-- Option 03 -->
<section class="label label--three">
  <div class="label__top-rule"></div>
  <div class="wave-art" role="img" aria-label="Flowing pink and yellow line waves"></div>
  <div class="about">
    <h2 class="about__title">About Product</h2>
    <p class="about__text">All plants source protein powderAll plants source protein powderAll plants source protein powderAll plants source protein powderAll plants source protein powderAll plants source protein powderAll plants source protein powderAll plants source protein powderAll plants source protein powderAll plants source protein powderAll plants source protein powderAll plants source protein powder</p>
  </div>
  <div class="company">
    <div class="company__name">Company name</div>
    <div class="company__line">Address</div>
    <div class="company__line">00000000</div>
    <div class="company__line">Tel : 00000000000</div>
    <div class="company__line">E-mail : hello@verde.lk</div>
    <div class="company__line">Web : 000000000000</div>
  </div>

  <div class="front-panel">
    <svg width="256" height="262" viewBox="0 0 256 262">
      <defs><linearGradient id="g3" x1="0" y1="0" x2="0" y2="1"><stop offset="0" stop-color="#2b6b14"/><stop offset="1" stop-color="#1d5210"/></linearGradient></defs>
      <path d="M0 0H256V212Q128 250 0 212Z" fill="url(#g3)"/>
      <path d="M0 184Q130 160 256 182V192Q130 172 0 198Z" fill="#fff"/>
      <path d="M0 196Q130 172 256 192V200Q130 182 0 208Z" fill="var(--swoosh)"/>
      <path d="M0 208Q130 186 256 204V210Q130 194 0 216Z" fill="var(--swoosh-soft)"/>
      <circle cx="128" cy="203" r="31" fill="#2b6b14" stroke="#fff" stroke-width="2"/>
    </svg>
    <h1 class="front-panel__title"><span class="t-all">ALL PLANT</span><span class="t-source">SOURCE PROTEIN</span><span class="t-powder">POWDER</span></h1>
    <div class="front-panel__weight">300g</div>
    <div class="front-panel__brand">VERDE</div>
  </div>

  <div class="produce" role="img" aria-label="Photo of soybeans, edamame pods, kale and broccoli"></div>
  <div class="produce--corner-left" role="img" aria-label="Photo of kale leaves"></div>
  <div class="produce--corner-right" role="img" aria-label="Photo of kale leaves"></div>

  <div class="ingredients">
    <div class="ingredients__tag">
      <div class="ingredients__title">Ingredients</div>
      <div class="ingredients__list">soybean, kale and broccoli<br>No Additives or Preservatives</div>
    </div>
    <svg class="ingredients__arrows" width="52" height="44" viewBox="0 0 52 44">
      <path d="M0 0H22L34 22L22 44H0Z" fill="var(--tag)"/>
      <path d="M24 0H34L46 22L34 44H24L36 22Z" fill="var(--tag-arrow)"/>
    </svg>
  </div>

  <div class="nutrition">
    Serving Size of 1 Tablespoon<br>Serving Per Container
    <div class="nutrition__rule"></div>
    Amount Per Serving<br>Calaries 125 Calaries from Fat 125
    <div class="nutrition__rule"></div>
    Total Fat 00<br>Saturated Fat 00<br>Polyunsturated Fat 00<br>Monounsaturated Fat 00<br>Cholostrerol 00 mg<br>Dodelum 00mg<br>Total Carbohydrates 00g<br>Protein 00 mg
  </div>

  <div class="batch-frame">
    <svg width="56" height="160" viewBox="0 0 56 160"><rect x="2" y="2" width="52" height="156" rx="8" fill="none" stroke="var(--gold)" stroke-width="2"/></svg>
    <div class="batch-frame__text">Best before :<br>Date of manufactured :<br>Batch No :<br>Maximum Price :</div>
  </div>

  <div class="badges"><span class="b1"></span><span class="b2"></span><span class="b3"></span><span class="b4"></span></div>
  <div class="label__base-band"></div>
</section>

</body>
</html>
```